Law Firm Needs a new Website Design

We need a new website design for our law firm located in Manhattan (Law Offices of Tobias R. Venkland, PLLC).
We have an existing logo that we will to continue using, which can be found in www.VenklandLaw.example.
The Prime Counsel, Top Advocates Logo should also be reflected near the bottom of the Home page.
The website will be 6 pages.

Deliverables:
I want a
1) home page,
2) About Us/Practice Areas page,
3) attorneys,
4) News and Articles page, and
5) Contact and Directions/Privacy Policy page.

The colors of my logo should be in the website.
I also like a touch of black and red.

The website should project "excellence."
We seek to provide the highest quality legal services.
We handle estate planning, wills, trusts, planning for people with disabilities, asset protection and preservation, Medicaid planning, hospital safe discharge, nursing home placement, powers of attorney, health care proxies, living wills, guardianships, probate, estate administration and related litigation.

I would like the colors of my Logo used (including shading where appropriate).
I also want some black on the borders and/or bottom and some red touches throughout the page.

My Logo should appear everywhere that "Law Offices Of Tobias R. Venkland, PLLC" appears.
I want the badges for Prime counsel, Top Advocates, Top Legal Practices, and ZELQ on the Home page.
I do not want too much text on the home page.

We would also like the website to have coding.
The final design should also communicate quality, expertise and stability.
Great start so far by the people who submitted designs.
Thank you.

Industry/Entity Type

Law Firm

Coding

Coded - Design and coding required

Number of Pages Required

5+ page

Colors
3276b5
ec1f27
474747

Requirements
Must have
• Please use my logo each time you mention Law Offices of Tobias R. Venkland, PLLC. Please include the Primecounsel, Top Advocates, Top Legal Practices and Zelq rating Badges on the web home page. I only wish to be contacted by phone. I am not including testimonials and am only using the New York City address.
Nice to have
• Prefer illustrations to photos regarding practice areas
Should not have
• Testimonials, contact me by email, free consultation.

```html
<!DOCTYPE html>
<html lang="en">
<head>
<meta charset="utf-8">
<title>Venkland Law — Estate Planning & Elder Law, Manhattan</title>
<link rel="stylesheet" href="https://fonts.googleapis.com/css2?family=Libre+Baskerville:wght@400;700&family=Montserrat:wght@400;600;700&family=Open+Sans:wght@400;600&display=swap">
<style>
:root{
  --navy:#23283a;
  --navy-deep:#1d2130;
  --logo-blue:#2b3f6e;
  --red:#a50d12;
  --red-bright:#c0141b;
  --ink:#2b2b2b;
  --body:#555a62;
  --muted:#9a9ea6;
  --pale:#f0f3f6;
  --grey-band:#e9ebee;
  --field:#f4f5f7;
  --line:#d3d6db;
  --white:#ffffff;
}
*{box-sizing:border-box;margin:0;padding:0}
html,body{width:1200px;height:3396px;overflow:hidden}
body{position:relative;background:var(--white);font-family:"Open Sans",Arial,sans-serif;color:var(--body)}
.abs{position:absolute}

/* header */
.site-header{left:0;top:0;width:1200px;height:104px;background:var(--white)}
.brand{left:100px;top:26px;display:flex;align-items:center;gap:16px}
.brand-square{width:40px;height:40px;background:var(--logo-blue);flex:none}
.brand-name{font-family:"Libre Baskerville",Georgia,serif;color:var(--logo-blue);font-size:17px;line-height:20px;font-weight:400;white-space:nowrap}
.brand-name small{display:block;font-size:12px;line-height:14px}
.social-bar{left:928px;top:0;width:170px;height:32px;background:var(--red);display:flex;justify-content:space-around;align-items:center;padding:0 12px}
.social-bar span{width:16px;height:16px;background:var(--white)}
.main-nav{right:100px;top:44px;display:flex;gap:34px;font-family:"Montserrat",Arial,sans-serif;font-size:12px;color:#333;letter-spacing:.3px}
.main-nav a{color:inherit;text-decoration:none;padding-bottom:8px}
.main-nav a.active{color:var(--red);border-bottom:2px solid var(--red)}

/* hero */
.hero{left:0;top:104px;width:1200px;height:598px;background:linear-gradient(90deg,#8e949c 0%,#b8bcc2 35%,#6b6f77 62%,#2a2c32 100%)}
.hero h1{left:100px;top:196px;font-family:"Libre Baskerville",Georgia,serif;font-weight:400;font-size:48px;line-height:60px;color:var(--white);letter-spacing:1px}
.hero p{left:100px;top:320px;font-size:11.5px;color:var(--white);letter-spacing:.2px;white-space:nowrap}
.btn-outline{display:flex;align-items:center;justify-content:center;border:2px solid currentColor;font-family:"Montserrat",Arial,sans-serif;font-weight:700;font-size:11px;letter-spacing:.5px;text-transform:uppercase}
.hero .btn-outline{left:100px;top:367px;width:152px;height:34px;color:var(--white)}
.slider-dots{left:100px;top:444px;display:flex;gap:7px}
.slider-dots span{width:8px;height:8px;border-radius:50%;border:1px solid var(--white)}
.slider-dots span:first-child{background:var(--white)}

/* quick band */
.quick-band{left:0;top:702px;width:1200px;height:102px;background:var(--navy)}
.select{top:40px;height:33px;border:2px solid var(--white);color:var(--white);font-family:"Montserrat",Arial,sans-serif;font-size:11px;font-weight:600;display:flex;align-items:center;justify-content:space-between;padding:0 16px}
.select svg{width:10px;height:10px}

/* consultation card */
.consult{left:718px;top:595px;width:385px;height:634px;background:var(--grey-band);box-shadow:0 4px 18px rgba(0,0,0,.12);z-index:2}
.consult-head{height:107px;background:var(--white);display:flex;align-items:center;justify-content:center;gap:14px}
.consult h2{margin:40px 0 0 46px;font-family:"Libre Baskerville",Georgia,serif;font-size:17px;font-weight:700;color:var(--ink);letter-spacing:1px}
.consult form{margin:18px 40px 0 46px}
.field{height:40px;background:var(--field);border:1px solid var(--line);margin-bottom:8px;font-size:11px;color:var(--muted);padding:11px 14px}
.field.msg{height:154px}
.submit{margin-top:14px;height:40px;background:var(--red);color:var(--white);font-family:"Montserrat",Arial,sans-serif;font-weight:700;font-size:13px;display:flex;align-items:center;justify-content:center}

/* shared headings */
.section-title{font-family:"Libre Baskerville",Georgia,serif;font-weight:700;letter-spacing:.5px;text-transform:uppercase;white-space:nowrap}

/* firm profile */
.profile{left:0;top:804px;width:1200px;height:482px;background:var(--pale)}
.profile h2{left:100px;top:78px;font-size:27px;color:var(--ink)}
.profile p{left:100px;top:124px;width:530px;font-size:13.5px;line-height:26px;color:var(--body)}
.profile p em{font-style:normal;color:var(--red)}
.btn-red{color:var(--red)}
.profile .btn-outline{left:100px;top:362px;width:152px;height:34px}

/* legal help */
.legal-help{left:0;top:1286px;width:1200px;height:380px;background:linear-gradient(90deg,#2c2b2c 0%,#4a4644 50%,#2e2c2d 100%)}
.legal-help h2{left:0;width:1200px;top:112px;text-align:center;font-family:"Libre Baskerville",Georgia,serif;font-weight:700;font-size:34px;color:var(--white);letter-spacing:1px}
.legal-help p{left:0;width:1200px;top:177px;text-align:center;font-size:17px;color:#d8d8d8}
.legal-help .btn-outline{left:489px;top:248px;width:222px;height:33px;color:var(--white)}

/* services */
.services{left:0;top:1666px;width:1200px;height:594px;background:var(--white)}
.services-head{left:100px;top:72px;display:flex;align-items:baseline;gap:18px}
.services-head h2{font-size:28px;color:var(--red)}
.services-head .tagline{font-family:"Montserrat",Arial,sans-serif;font-size:24px;color:#555;white-space:nowrap}
.services .rule{left:100px;top:140px;width:1000px;height:5px;background:#cfd2d6}
.service{width:300px}
.service h3{font-family:"Montserrat",Arial,sans-serif;font-weight:700;font-size:17px;color:var(--ink);border-left:4px solid var(--red);padding-left:8px;line-height:18px}
.service p{margin-top:10px;font-size:13px;line-height:23px;color:var(--muted)}
.services .btn-outline{left:95px;top:489px;width:163px;height:33px}

/* news */
.news{left:0;top:2260px;width:1200px;height:588px;background:var(--grey-band)}
.news h2{left:100px;top:62px;font-size:28px;color:var(--red)}
.news .sub{left:100px;top:108px;font-size:12.5px;color:#555;letter-spacing:.2px}
.news-card{top:153px;width:272px}
.news-photo{width:272px;height:191px;position:relative}
.news-avatar{position:absolute;right:14px;bottom:-20px;width:66px;height:66px;border-radius:50%;border:3px solid var(--white);background:#b9a48f}
.news-card .date{margin-top:25px;font-size:12px;color:#555}
.news-card h3{margin-top:22px;font-family:"Montserrat",Arial,sans-serif;font-weight:700;font-size:17px;color:var(--ink)}
.news-card p{margin-top:8px;font-size:12.5px;line-height:22px;color:var(--muted)}
.news-card .more{margin-top:8px;font-size:12px;color:var(--red);text-transform:uppercase}

/* partners */
.partners{left:0;top:2848px;width:1200px;height:154px;background:#eeeff1}
.partners h2{left:100px;top:79px;font-size:22px;color:var(--red)}
.badge{background:var(--white);border:1px solid #c9ccd1}
.partners .arrow{left:1078px;top:62px;width:22px;height:34px}

/* footer */
.site-footer{left:0;top:3002px;width:1200px;height:326px;background:var(--navy)}
.site-footer h4{font-family:"Montserrat",Arial,sans-serif;font-weight:700;font-size:17px;color:var(--white);letter-spacing:.3px}
.foot-list{margin-top:14px;font-size:12.5px;line-height:27px;color:#dfe1e6;list-style:none;white-space:nowrap}
.site-footer .blurb{margin-top:14px;width:270px;font-size:13px;line-height:25px;color:#dfe1e6}
.signup-field{left:833px;top:161px;width:267px;height:41px;background:var(--white);font-size:11px;color:var(--muted);padding:13px 14px}
.signup-btn{left:992px;top:222px;width:108px;height:40px;background:var(--red);color:var(--white);font-family:"Montserrat",Arial,sans-serif;font-size:12px;font-weight:600;display:flex;align-items:center;justify-content:center;border:1px solid #d33}
.bottom-bar{left:0;top:3328px;width:1200px;height:68px;background:var(--navy-deep);border-top:1px solid #3a3f52}
.bottom-bar .copy{left:100px;top:25px;font-size:11px;color:#8d93a3}
.bottom-bar .mark{left:582px;top:-28px;width:36px;height:36px;background:var(--logo-blue);border:2px solid #5a6f9e}
.bottom-bar .legal{right:100px;top:25px;display:flex;gap:26px;font-size:11px;color:#c5c9d3;text-transform:uppercase}
</style>
</head>
<body>

<header class="site-header abs">
  <div class="brand abs">
    <span class="brand-square"></span>
    <span class="brand-name"><small>Law Offices of</small>Tobias R. Venkland<small>PLLC</small></span>
  </div>
  <div class="social-bar abs" aria-label="Social links"><span></span><span></span><span></span><span></span></div>
  <nav class="main-nav abs">
    <a class="active">HOME</a><a>ABOUT</a><a>SERVICE</a><a>PRACTICE AREAS</a><a>PRIVACY POLICY</a><a>NEWS</a><a>CONTACT</a>
  </nav>
</header>

<section class="hero abs" role="img" aria-label="Attorney in a dark suit and red tie holding an open law book">
  <h1 class="abs">WELCOME<br>VENKLAND LAW</h1>
  <p class="abs">WE CARE ABOUT OUR CLIENTS AND BELIEVE IN CULTIVATING LONG-TERM RELATIONSHIPS</p>
  <div class="btn-outline abs">Learn More</div>
  <div class="slider-dots abs"><span></span><span></span><span></span><span></span><span></span></div>
</section>

<div class="quick-band abs">
  <div class="select abs" style="left:100px;width:172px">ATTORNEYS <svg viewBox="0 0 10 10"><path d="M1 3l4 4 4-4" fill="none" stroke="#fff" stroke-width="1.5"/></svg></div>
  <div class="select abs" style="left:303px;width:243px">CONTACT AND DIRECTIONS <svg viewBox="0 0 10 10"><path d="M1 3l4 4 4-4" fill="none" stroke="#fff" stroke-width="1.5"/></svg></div>
</div>

<aside class="consult abs">
  <div class="consult-head">
    <span class="brand-square" style="width:34px;height:34px"></span>
    <span class="brand-name" style="font-size:16px"><small>Law Offices of</small>Tobias R. Venkland<small>PLLC</small></span>
  </div>
  <h2>CASE CONSULTATION</h2>
  <form>
    <div class="field">Name</div>
    <div class="field">Phone</div>
    <div class="field">Your Email</div>
    <div class="field msg">Message</div>
    <div class="submit">SUBMIT</div>
  </form>
</aside>

<section class="profile abs">
  <h2 class="section-title abs">Firm Profile</h2>
  <p class="abs">Our firm was founded in 1993 by <em>Tobias R. Venkland</em>, a member of the National Guild of Elder Care Counsel (NGECC) and an elder law practitioner for over 19 years. Our firm is uniquely positioned to provide quality legal advice and representation in regards to estate planning, wills, trusts, planning for people with disabilities, asset protection and preservation, Medicaid planning, hospital safe discharge, nursing home placement, powers of attorney, health care proxies, living wills, guardianships, probate, estate administration and related litigation.</p>
  <div class="btn-outline btn-red abs">Learn More</div>
</section>

<section class="legal-help abs" role="img" aria-label="Dim courthouse interior with columns and a classical statue">
  <h2 class="abs">LEGAL HELP ?</h2>
  <p class="abs">We Care About Our Clients and Believe in Cultivating Long-Term Relationships.</p>
  <div class="btn-outline abs">Contact Us Now</div>
</section>

<section class="services abs">
  <div class="services-head abs">
    <h2 class="section-title">Our Services</h2>
    <span class="tagline">We Handle Estate Planning</span>
  </div>
  <div class="rule abs"></div>
  <div class="service abs" style="left:100px;top:195px"><h3>WILLS</h3><p>Our Familiarity with Entitlement Programs Such as Medicaid and the Statutes and Regulations Pertaining to Them.</p></div>
  <div class="service abs" style="left:460px;top:195px"><h3>TRUSTS</h3><p>Our Familiarity with Entitlement Programs Such as Medicaid and the Statutes and Regulations Pertaining to Them.</p></div>
  <div class="service abs" style="left:817px;top:195px"><h3>MEDICAID PLANNING</h3><p>Our Familiarity with Entitlement Programs Such as Medicaid and the Statutes and Regulations Pertaining to Them.</p></div>
  <div class="service abs" style="left:100px;top:349px"><h3>POWERS OF ATTORNEY</h3><p>Our Familiarity with Entitlement Programs Such as Medicaid and the Statutes and Regulations Pertaining to Them.</p></div>
  <div class="service abs" style="left:460px;top:349px"><h3>PROBATE</h3><p>Our Familiarity with Entitlement Programs Such as Medicaid and the Statutes and Regulations Pertaining to Them.</p></div>
  <div class="service abs" style="left:817px;top:349px"><h3>LIVING WILLS</h3><p>Our Familiarity with Entitlement Programs Such as Medicaid and the Statutes and Regulations Pertaining to Them.</p></div>
  <div class="btn-outline btn-red abs">Read More</div>
</section>

<section class="news abs">
  <h2 class="section-title abs">Latest News</h2>
  <span class="sub abs">OUR FIRM WAS FOUNDED IN 1993 BY TOBIAS R. VENKLAND</span>
  <article class="news-card abs" style="left:100px">
    <div class="news-photo" role="img" aria-label="Courtroom hearing with judge and attorneys" style="background:linear-gradient(135deg,#7a5a3e,#b58b64 55%,#4a3526)"><span class="news-avatar" role="img" aria-label="Author portrait"></span></div>
    <div class="date">Posted April 3, 2016</div>
    <h3>LATEST NEWS</h3>
    <p>We care about our clients and believe in cultivating long-term relationships...</p>
    <div class="more">Read More</div>
  </article>
  <article class="news-card abs" style="left:457px">
    <div class="news-photo" role="img" aria-label="Hands in handcuffs" style="background:linear-gradient(135deg,#d8cfc6,#a9867a 50%,#6f7f95)"><span class="news-avatar" role="img" aria-label="Author portrait"></span></div>
    <div class="date">Posted April 3, 2016</div>
    <h3>LATEST NEWS</h3>
    <p>We care about our clients and believe in cultivating long-term relationships...</p>
    <div class="more">Read More</div>
  </article>
  <article class="news-card abs" style="left:815px">
    <div class="news-photo" role="img" aria-label="Judge with gavel and scales of justice" style="background:linear-gradient(135deg,#1c1c1e,#3b342c 55%,#9b7a3e)"><span class="news-avatar" role="img" aria-label="Author portrait" style="background:#d9a07a"></span></div>
    <div class="date">Posted April 3, 2016</div>
    <h3>LATEST NEWS</h3>
    <p>We care about our clients and believe in cultivating long-term relationships...</p>
    <div class="more">Read More</div>
  </article>
</section>

<section class="partners abs">
  <h2 class="section-title abs">Our Partner</h2>
  <div class="badge abs" role="img" aria-label="Prime Counsel badge" style="left:374px;top:60px;width:210px;height:43px"></div>
  <div class="badge abs" role="img" aria-label="Top Advocates badge" style="left:643px;top:60px;width:206px;height:43px"></div>
  <div class="abs" role="img" aria-label="Top Legal Practices badge" style="left:906px;top:30px;width:102px;height:92px;background:#2a4b8c"></div>
  <svg class="arrow abs" viewBox="0 0 22 34" aria-hidden="true"><path d="M4 3l14 14L4 31" fill="none" stroke="#b9bcc2" stroke-width="3"/></svg>
</section>

<footer class="site-footer abs">
  <div class="abs" style="left:100px;top:64px">
    <h4>SITE MAP</h4>
    <ul class="foot-list"><li>Home</li><li>Practice Areas</li><li>Privacy Policy</li><li>Contact and Directions</li><li>News</li><li>Attorneys</li></ul>
  </div>
  <div class="abs" style="left:355px;top:64px">
    <h4>ADDRESS</h4>
    <ul class="foot-list"><li>Manhattan Main Office :</li><li>318 Harlow Avenue Suite 1204</li><li>New York NY 10127</li><li>Tel: (212) 555-0148</li><li>Fax: (212) 555-0172</li></ul>
  </div>
  <div class="abs" style="left:573px;top:92px">
    <ul class="foot-list"><li>Long Island Office :</li><li>742 Orchard Lane</li><li>suite 210</li><li>Elmstead, NY 11598</li><li>Tel: (212) 555-0148</li></ul>
  </div>
  <div class="abs" style="left:833px;top:64px">
    <h4>STAY CONNECTED</h4>
    <p class="blurb">We care about our clients and believe in cultivating long-term relationships.</p>
  </div>
  <div class="signup-field abs">Your Email Address</div>
  <div class="signup-btn abs">SIGN UP</div>
</footer>

<div class="bottom-bar abs">
  <span class="copy abs">Copyrights© 2009-2016 Law Offices of Tobias R. Venkland, PLLC</span>
  <span class="mark abs"></span>
  <div class="legal abs"><span>Privacy Policy</span><span>Terms and Conditions</span></div>
</div>

</body>
</html>
```